I need to present the newly formed Maple Tap concept at a board meeting in 1 weeks time. Maple Tap is an American gas station Themed dispense concept for wine .. I need a max of 12 page power point template that incorporates a number of the photo elements of the concept and Has the uva rapida logo on each slide .. I have more pics of the concept that I will forward if you accept the project

```html
<!DOCTYPE html>
<html lang="en">
<head>
<meta charset="utf-8">
<title>Maple Tap – Title Slide</title>
<link rel="stylesheet" href="https://fonts.googleapis.com/css2?family=Archivo+Black&family=Arimo:wght@400;700&display=swap">
<style>
  :root {
    --paper: #ffffff;
    --ink: #111111;
    --cream: #fff8e0;
    --butter: #fee79a;
    --sun: #fdcf2a;
    --amber-start: #fdca0a;
    --amber-mid: #fdb80e;
    --amber-end: #fca30d;
    --brand-red: #e8352a;
    --white: #ffffff;
  }
  * { margin: 0; padding: 0; box-sizing: border-box; }
  html, body {
    width: 1200px; height: 1200px; overflow: hidden;
    background: var(--paper);
  }
  .sheet { position: relative; width: 1200px; height: 1200px; }
  .page-label {
    position: absolute; top: 112px; left: 0; width: 100%;
    text-align: center;
    font-family: "Arimo", Arial, sans-serif;
    font-size: 44px; color: var(--ink);
  }
  .slide {
    position: absolute; left: 125px; top: 235px;
    width: 917px; height: 649px; overflow: hidden;
    background: radial-gradient(ellipse 75% 80% at 55% 38%,
      var(--cream) 0%, var(--butter) 65%, var(--sun) 100%);
  }
  .brand-name {
    position: absolute; left: 47px; top: 44px;
    font-family: "Arimo", Arial, sans-serif;
    font-weight: 700; font-size: 38px; line-height: 1;
    color: var(--brand-red);
  }
  .title-panel {
    position: absolute; left: 256px; top: 172px;
    width: 570px; height: 341px;
    background: linear-gradient(90deg, var(--amber-start) 0%, var(--amber-start) 25%,
      var(--amber-mid) 60%, var(--amber-end) 100%);
  }
  .pump-illustration {
    position: absolute; left: 178px; top: 148px;
    width: 121px; height: 368px;
  }
  .title-text {
    position: absolute; left: 344px; top: 254px;
    color: var(--white);
  }
  .title-text .presentation-name {
    font-family: "Archivo Black", "Arial Black", sans-serif;
    font-weight: 400; font-size: 31px; line-height: 1.25; letter-spacing: 0.4px;
  }
  .title-text .company-name {
    font-family: "Arimo", Arial, sans-serif;
    font-weight: 700; font-size: 32px; line-height: 1.25;
  }
  .footer-band {
    position: absolute; left: 0; top: 580px;
    width: 917px; height: 69px;
    background: linear-gradient(90deg, var(--amber-start) 0%, var(--amber-start) 22%,
      var(--amber-mid) 60%, var(--amber-end) 100%);
  }
</style>
</head>
<body>
  <div class="sheet">
    <p class="page-label">Page 1</p>
    <section class="slide">
      <div class="brand-name">Maple Tap</div>
      <div class="title-panel"></div>
      <svg class="pump-illustration" viewBox="0 0 121 368" role="img" aria-label="Illustration of a vintage teal and cream gas pump with hose">
        <defs>
          <linearGradient id="pumpTone" x1="0" y1="0" x2="1" y2="0">
            <stop offset="0" stop-color="#6cc9bd"/>
            <stop offset="0.15" stop-color="#ece8d6"/>
            <stop offset="0.7" stop-color="#e2ddc8"/>
            <stop offset="1" stop-color="#5cb8ac"/>
          </linearGradient>
        </defs>
        <rect x="0" y="0" width="121" height="368" rx="10" fill="url(#pumpTone)"/>
      </svg>
      <div class="title-text">
        <h1 class="presentation-name">Name Of Presentasion</h1>
        <p class="company-name">Company Name</p>
      </div>
      <div class="footer-band"></div>
    </section>
  </div>
</body>
</html>
```